Detailing informational flyer

I want to design a new flyer for my automotive detailing business. The flyer should use the color scheme from the logo and be easy to read and understand the services we offer.

Font styles to use
Serif
Sans Serif

Colors
3176b5
0255a3
fbed22
33a6d7
0692cd
ffffff

Requirements
Must have
• must include all information from the copy
Nice to have
• include a Glenvaro logo such as the image attached

```html
<!DOCTYPE html>
<html lang="en">
<head>
<meta charset="utf-8">
<title>Detailing and Oil Change Flyers</title>
<link href="https://fonts.googleapis.com/css2?family=Archivo+Black&family=Lato:wght@400;700;900&family=Montserrat:wght@700;800&display=swap" rel="stylesheet">
<style>
:root{
  --stage:#2a2a2a;
  --blue-deep:#0255a3;
  --blue-mid:#3176b5;
  --blue-sky:#33a6d7;
  --blue-bright:#0692cd;
  --blue-navy:#0b3d8f;
  --yellow:#fbed22;
  --red:#d8262e;
  --slate:#3a4450;
  --white:#ffffff;
  --ink:#333b45;
  --paper-shade:#e6ebf0;
}
*{box-sizing:border-box;margin:0;padding:0}
html,body{width:958px;height:1200px;overflow:hidden;background:var(--stage)}
.stage{position:relative;width:958px;height:1200px}
.flyer{position:absolute;top:287px;width:498px;height:708px;transform-origin:0 0;transform:scale(0.884);overflow:hidden;background:var(--white);font-family:"Lato",sans-serif;color:var(--ink)}
.flyer--detail{left:26px}
.flyer--lube{left:492px}
.abs{position:absolute}
.photo{position:absolute;left:0;top:0;width:498px;height:305px}
.photo--wash{background:linear-gradient(120deg,#d9dde2 0%,#b9c3cf 35%,#2f5aa8 45%,#c9ccd2 55%,#b0232c 80%,#e8e0e0 100%)}
.photo--engine{height:300px;background:linear-gradient(160deg,#c9ccd0 0%,#8d939a 30%,#2c2f33 60%,#1a1c1f 100%)}
.brand-box{position:absolute;left:282px;top:0;width:216px;display:flex;flex-direction:column;align-items:center;justify-content:center;gap:6px}
.brand-box--detail{height:160px;background:#6fb0ea}
.brand-box--lube{height:290px;background:var(--slate)}
.brand-dot{width:40px;height:40px;border-radius:50%}
.brand-name{font-family:"Montserrat",sans-serif;font-weight:800;font-size:17px;letter-spacing:.5px}
.brand-name--detail{color:var(--yellow)}
.brand-name--lube{color:var(--red)}
.paper{position:absolute;left:0;width:498px;background:linear-gradient(180deg,var(--white) 0%,var(--paper-shade) 100%)}
.ribbon{position:absolute;left:24px;top:258px}
.ribbon-icon{position:absolute;left:46px;width:50px;height:50px;border-radius:50%;background:#8a98a8;border:3px solid var(--white);display:flex;align-items:center;justify-content:center}
.ribbon-icon span{width:24px;height:12px;border-radius:6px 6px 2px 2px;background:var(--white)}
.copy{position:absolute;left:125px;width:350px}
.copy-title{font-family:"Montserrat",sans-serif;font-weight:800;font-size:13.5px;color:var(--blue-navy)}
.copy-sub{font-family:"Montserrat",sans-serif;font-weight:700;font-size:12.5px;color:var(--blue-bright)}
.service h3{font-size:9.5px;font-weight:700;color:var(--blue-deep);margin-bottom:4px}
.service p{font-size:6.6px;line-height:1.4;color:#444}
.partner{position:absolute;left:150px;top:612px;font-family:"Montserrat",sans-serif;font-weight:800;font-size:20px;color:var(--red)}
.phone{position:absolute;display:flex;align-items:center;gap:7px;font-size:15px;color:#1d2a3a}
.phone svg{width:15px;height:15px}
.foot{position:absolute;left:0;bottom:0;width:498px;height:40px;background:var(--blue-navy);display:flex;align-items:center;justify-content:center;gap:6px;color:var(--white);font-size:11.5px}
.foot svg{width:11px;height:12px}
.offer-title{position:absolute;left:31px;top:343px;font-family:"Archivo Black",sans-serif;font-size:20px;line-height:27px;letter-spacing:.6px}
.offer-title .main{color:var(--blue-deep);display:block}
.offer-title .accent{color:var(--red);display:block}
.checklist{position:absolute;list-style:none;font-size:9px;text-transform:uppercase;color:#2f3640}
.checklist li{display:flex;height:25px;align-items:flex-start}
.checklist b{color:var(--blue-deep);width:22px;flex:none;font-weight:700}
</style>
</head>
<body>
<main class="stage">

  <!-- Detailing flyer -->
  <article class="flyer flyer--detail">
    <div class="photo photo--wash" role="img" aria-label="Smiling attendant in blue work wear washing a soapy red car"></div>
    <div class="brand-box brand-box--detail">
      <div class="brand-dot" style="background:var(--yellow)"></div>
      <div class="brand-name brand-name--detail">RIDGEWAY CARWASH</div>
    </div>
    <div class="paper" style="top:300px;height:368px"></div>
    <svg class="abs" style="left:0;top:250px" width="498" height="80" viewBox="0 0 498 80">
      <path d="M0 40 Q250 0 498 30 L498 80 L0 80 Z" fill="var(--white)"/>
      <path d="M0 28 Q250 -8 498 18 L498 30 Q250 2 0 40 Z" fill="var(--yellow)"/>
      <path d="M0 22 Q250 -14 498 10 L498 18 Q250 -8 0 28 Z" fill="var(--blue-deep)"/>
    </svg>
    <svg class="ribbon" width="90" height="420" viewBox="0 0 90 420">
      <path d="M0 0 H70 L90 12 V420 L45 395 L0 420 Z" fill="var(--blue-mid)"/>
      <path d="M70 0 L90 12 H70 Z" fill="var(--blue-navy)"/>
    </svg>
    <div class="ribbon-icon" style="top:340px"><span></span></div>
    <div class="ribbon-icon" style="top:410px"><span></span></div>
    <div class="ribbon-icon" style="top:483px"><span></span></div>
    <div class="ribbon-icon" style="top:555px"><span></span></div>

    <div class="copy" style="top:302px">
      <div class="copy-title">ASK TO SPEAK TO A MANAGER</div>
      <div class="copy-sub">about scheduling any of our detailing services.</div>
    </div>
    <section class="copy service" style="top:345px">
      <h3>Exterior detailing includes:</h3>
      <p>We wash, clay, compound, polish, and wax, as needed to restore the deep rich gloss and provide a durable shine for that "new car" look. This process removes light oxidation from the vehicle and protects the clear coat finish. Finishing touches include rim cleaning and tire shine.</p>
    </section>
    <section class="copy service" style="top:412px">
      <h3>Interior detailing shampoo includes:</h3>
      <p>We perform a deep cleaning of the interior such as the dashboard, door jams, center console, trunk area, upholstered seats, and all carpets and mats. This process will remove soils and most stains. Windows are cleaned inside and out. All leather is dressed to provide a protective finish. Air fresher is available upon request.</p>
    </section>
    <section class="copy service" style="top:488px">
      <h3>Mini detail/ VIP service includes:</h3>
      <p>Ridgeway Special Wash with triple polish wax, Glenvaro Shield protectant, tire shine, and a detailed and gentle cleaning of the upholstery. 4 rubber or carpet mats are shampooed. All interior surfaces are dressed including dashboard, door panels, center console. This is followed by a detailed carpet and upholstery vacuum with compressed air to remove dirt from hard to reach places. For added shine ask about adding on our express wax service to your mini detail package.</p>
    </section>
    <section class="copy service" style="top:562px">
      <h3>Headlight restoration:</h3>
      <p>This shop proudly offers the Headlight Service, which can polish or restore your headlight to a clear, safe condition at a fraction of the cost of headlight replacement! Restore the lens to a clear, shiny &amp; safe condition.</p>
    </section>
    <div class="partner">GLENVARO</div>
    <div class="phone" style="left:290px;top:620px">
      <svg viewBox="0 0 16 16"><circle cx="8" cy="8" r="7.2" fill="none" stroke="var(--blue-deep)" stroke-width="1.4"/><path d="M5.5 4.5 L7 6 L6.2 7.2 Q7.2 9 8.8 9.8 L10 9 L11.5 10.5 L10.6 11.6 Q7.5 11.5 4.5 6.5 Z" fill="var(--blue-deep)"/></svg>
      +1 555-014-2290
    </div>
    <svg class="abs" style="left:0;top:640px" width="498" height="30" viewBox="0 0 498 30">
      <path d="M0 30 Q260 10 498 0 L498 8 Q260 18 0 30 Z" fill="var(--yellow)"/>
      <path d="M0 30 Q260 16 498 8 L498 30 Z" fill="var(--blue-navy)"/>
    </svg>
    <footer class="foot">
      <svg viewBox="0 0 12 14"><path d="M6 0 A5 5 0 0 1 11 5 C11 9 6 14 6 14 C6 14 1 9 1 5 A5 5 0 0 1 6 0 Z" fill="var(--yellow)"/><circle cx="6" cy="5" r="2" fill="var(--blue-navy)"/></svg>
      48-20 Linden Pkwy Maple Heights 11402
    </footer>
  </article>

  <!-- Oil change flyer -->
  <article class="flyer flyer--lube">
    <div class="photo photo--engine" role="img" aria-label="Hand pouring golden motor oil from a silver jug into an engine"></div>
    <div class="brand-box brand-box--lube">
      <div class="brand-dot" style="background:var(--red)"></div>
      <div class="brand-name brand-name--lube">QUICKFLOW LUBE</div>
    </div>
    <div class="paper" style="top:330px;height:340px"></div>
    <svg class="abs" style="left:0;top:285px" width="498" height="70" viewBox="0 0 498 70">
      <path d="M0 12 Q250 -8 498 30 L498 70 L0 70 Z" fill="var(--white)"/>
      <path d="M0 10 Q250 -12 498 24 L498 44 Q250 8 0 30 Z" fill="var(--red)"/>
      <path d="M0 28 Q250 6 498 42 L498 52 Q250 16 0 36 Z" fill="var(--blue-deep)"/>
      <path d="M0 36 Q250 16 498 52 L498 70 L0 70 Z" fill="var(--white)"/>
    </svg>
    <h2 class="offer-title"><span class="main">EVERY OIL CHANGE INCLUDES</span><span class="accent">A FREE CAR WASH</span></h2>
    <ol class="checklist" style="left:31px;top:405px;width:250px">
      <li><b>1.</b>Up to 5 qts. of Corvane bulk oil</li>
      <li><b>2.</b>Quality oil filter</li>
      <li><b>3.</b>Complete chassis lubrication</li>
      <li><b>4.</b>Check &amp; fill brake fluid</li>
      <li><b>5.</b>Check &amp; transmission fluid</li>
      <li><b>6.</b>Check &amp; fill different fluid</li>
      <li><b>7.</b>Check &amp; fill power steering fluid</li>
      <li><b>8.</b>Check &amp; fill washer fluid</li>
    </ol>
    <ol class="checklist" style="left:274px;top:405px;width:210px">
      <li><b>9.</b>Check &amp; fill antifreeze</li>
      <li style="height:37px"><b>10.</b><span>Check breather &amp; air filter<br>(charge if replaced)</span></li>
      <li style="height:38px"><b>11.</b><span>Check wiper blades<br>(charge if replaced)</span></li>
      <li><b>12.</b>Check tire pressure &amp; inflate</li>
      <li><b>13.</b>Lubricate door hinges</li>
      <li><b>14.</b>Computerized service record</li>
    </ol>
    <div class="phone" style="left:295px;top:598px">
      <svg viewBox="0 0 16 16"><circle cx="8" cy="8" r="7.2" fill="none" stroke="var(--blue-deep)" stroke-width="1.4"/><path d="M5.5 4.5 L7 6 L6.2 7.2 Q7.2 9 8.8 9.8 L10 9 L11.5 10.5 L10.6 11.6 Q7.5 11.5 4.5 6.5 Z" fill="var(--blue-deep)"/></svg>
      +1 555-014-2290
    </div>
    <svg class="abs" style="left:0;top:632px" width="498" height="40" viewBox="0 0 498 40">
      <path d="M0 40 Q260 30 498 0 L498 10 Q260 36 0 40 Z" fill="var(--red)"/>
      <path d="M0 40 Q260 36 498 10 L498 40 Z" fill="var(--blue-navy)"/>
    </svg>
    <footer class="foot">
      <svg viewBox="0 0 12 14"><path d="M6 0 A5 5 0 0 1 11 5 C11 9 6 14 6 14 C6 14 1 9 1 5 A5 5 0 0 1 6 0 Z" fill="var(--yellow)"/><circle cx="6" cy="5" r="2" fill="var(--blue-navy)"/></svg>
      48-20 Linden Pkwy Maple Heights 11402
    </footer>
  </article>

</main>
</body>
</html>
```